依頼詳細
PCとスマホデザインの両方納品をいただきますが、
まずはデザインイメージが確認しやすいPCページのみの提案をお願いします。
スマホページは当選者に納品時にお願いしたいと思います。
スマホサイズは横幅750pxのサイズで作成してください。

レスポンシブウェブデザインを意識したデザインでお願いします。

デザインに関しては、添付してあるデザインレイアウト設計シートを基にお願いします。
参考サイトのURLはデザインレイアウト設計シートに記載してあります。

画像データについては、フリー素材から流用してイメージ画像に当て込んでください。

足りない場合は、一旦他のサイトの写真をサンプルとして入れてください。
また、購入が必要な写真などを利用した場合、価格とサイト名を教えてください。
ページ数
1ページ
希望イメージ
シンプル 複雑
単色 カラフル
暗い 明るい
日常 高級
遊び心 厳粛
未来的 伝統的
女性的 男性的
納品ファイル
• イラストレーター形式 (.ai)
• フォトショップ形式 (.psd)
• PNG形式 (.png)
補足説明
上記のいずれか1つ(アウトラインありとなしの2つ)と高解像度JPGを納品お願いします。

クライアント様より選定いただきました。
一番イメージに近いものでした

ご提案ありがとうございました。
また機会がありましたら是非お願いします。

```html
<!DOCTYPE html>
<html lang="ja">
<head>
<meta charset="utf-8">
<title>青葉製作所</title>
<link rel="stylesheet" href="https://fonts.googleapis.com/css2?family=Noto+Sans+JP:wght@400;500;700&family=Noto+Serif+JP:wght@400;500;700&display=swap">
<style>
:root{
  --ink:#222;
  --muted:#777;
  --line:#d9d9d9;
  --green:#3f9a2d;
  --green-dark:#2f7f20;
  --red:#c40f0f;
  --grey-band:#e6e6e6;
  --logo-box:#e4e4e4;
  --white:#fff;
}
*{margin:0;padding:0;box-sizing:border-box}
html,body{width:1200px;height:2661px;overflow:hidden;background:var(--white)}
body{font-family:"Noto Sans JP",sans-serif;color:var(--ink);position:relative}
.serif{font-family:"Noto Serif JP",serif}

.site-header{position:absolute;top:0;left:0;width:1200px;height:56px;display:flex;align-items:center;justify-content:space-between;padding:0 48px 0 80px}
.logo{width:208px;height:30px;background:var(--logo-box);display:flex;align-items:center;justify-content:center;font-size:12px;color:var(--muted)}
.global-nav{display:flex;gap:26px;font-size:13px}

.hero{position:absolute;top:56px;left:0;width:1200px;height:632px;background:linear-gradient(160deg,#8d8f8a 0%,#6f6a5e 35%,#a38f66 55%,#5a5f63 80%,#3e4246 100%);display:flex;align-items:center;justify-content:center}
.hero-title{font-family:"Noto Serif JP",serif;font-size:34px;font-weight:500;color:var(--white);letter-spacing:1px;text-shadow:0 2px 6px rgba(0,0,0,.5);margin-top:-90px}

.section-label{position:absolute;left:0;width:1200px;text-align:center;font-size:11px;letter-spacing:2px;color:var(--green);font-family:"Noto Serif JP",serif}
.section-title{position:absolute;left:0;width:1200px;text-align:center;font-size:26px;font-family:"Noto Serif JP",serif;font-weight:500}

.about-photo{position:absolute;left:80px;top:848px;width:480px;height:304px;background:linear-gradient(135deg,#b7a35e 0%,#d8c790 40%,#8a7c55 70%,#4e4b40 100%)}
.about-text{position:absolute;left:610px;top:900px;width:500px}
.about-text h3{font-family:"Noto Serif JP",serif;font-size:22px;font-weight:500;line-height:1.65;margin-bottom:24px}
.about-text p{font-size:12px;line-height:2.1;color:#444;letter-spacing:.5px}

.outline-btn{position:absolute;left:460px;width:280px;height:48px;border:1px solid var(--green);display:flex;align-items:center;justify-content:center;font-size:13px;color:var(--green)}
.outline-btn::after{content:"";position:absolute;inset:4px;border:1px solid var(--green);opacity:.35}

.feature-band{position:absolute;top:1344px;left:0;width:1200px;height:296px;display:flex}
.feature{flex:1;position:relative;display:flex;flex-direction:column;justify-content:center;color:var(--white)}
.feature-products{background:linear-gradient(120deg,#4a4139 0%,#7b5a3e 45%,#3c3a38 100%);padding-left:260px}
.feature-cases{background:linear-gradient(120deg,#5a3b2a 0%,#9a6a44 50%,#3a3531 100%);padding-left:250px}
.feature .en{font-size:11px;letter-spacing:2px;font-family:"Noto Serif JP",serif}
.feature .ja{font-size:24px;font-family:"Noto Serif JP",serif;margin-top:4px}

.news-list{position:absolute;top:1832px;left:192px;width:816px;list-style:none}
.news-list li{display:flex;height:52px;align-items:center;border-bottom:1px solid var(--line);font-size:12px}
.news-list .date{width:108px;color:var(--muted)}

.shop-band{position:absolute;top:2288px;left:0;width:1200px;height:160px;background:var(--grey-band)}
.shop-btn{position:absolute;top:24px;width:452px;height:104px;display:flex;align-items:center;justify-content:center;color:var(--white);font-size:16px;font-weight:500}
.shop-btn::after{content:"";position:absolute;inset:6px;border:1px solid rgba(255,255,255,.6)}
.shop-official{left:120px;background:var(--green)}
.shop-mall{left:632px;background:var(--red)}

.site-footer{position:absolute;top:2448px;left:0;width:1200px;height:213px}
.footer-logo{position:absolute;left:80px;top:44px;width:200px;height:30px;background:var(--logo-box);display:flex;align-items:center;justify-content:center;font-size:12px;color:var(--muted)}
.footer-address{position:absolute;left:80px;top:86px;font-size:10px;line-height:1.8;color:#555}
.footer-nav{position:absolute;right:80px;top:70px;display:flex;gap:26px;font-size:11px}
.copyright{position:absolute;left:0;top:160px;width:1200px;text-align:center;font-size:9px;color:var(--muted)}
</style>
</head>
<body>

<header class="site-header">
  <div class="logo">青葉製作所</div>
  <nav class="global-nav">
    <span>事業紹介</span><span>製品情報</span><span>採用情報</span><span>会社案内</span><span>お問い合わせ</span>
  </nav>
</header>

<section class="hero" role="img" aria-label="倉庫の棚と物流用ラックの写真">
  <h1 class="hero-title">「物流と倉庫の収納・保管」の効率化・安全化を提案</h1>
</section>

<p class="section-label" style="top:744px">ABOUT</p>
<h2 class="section-title" style="top:768px">青葉製作所について</h2>

<div class="about-photo" role="img" aria-label="倉庫の棚に保管された段ボールと荷物の写真"></div>
<div class="about-text">
  <h3>「物流と倉庫の収納・保管」の効率化・安全化を<br>提案します。</h3>
  <p>テキストテキストテキストテキストテキストテキストテキストテキストテキストテキストテキストテキストテキストテキストテキストテキストテキストテキストテキストテキストテキストテキストテキストテキストテキストテキストテキストテキストテキストテキスト</p>
</div>

<a class="outline-btn" style="top:1208px">事業紹介</a>

<section class="feature-band">
  <div class="feature feature-products" role="img" aria-label="倉庫の棚とラックの写真">
    <span class="en">PRODUCT</span>
    <span class="ja">製品情報</span>
  </div>
  <div class="feature feature-cases" role="img" aria-label="物流倉庫の導入事例の写真">
    <span class="en">CASE STUDY</span>
    <span class="ja">導入事例</span>
  </div>
</section>

<p class="section-label" style="top:1724px">NEWS</p>
<h2 class="section-title" style="top:1748px">お知らせ</h2>

<ul class="news-list">
  <li><span class="date">20XX.00.00</span><span>テキストテキストテキストテキストテキストテキストテキストテキストテキストテキスト</span></li>
  <li><span class="date">20XX.00.00</span><span>テキストテキストテキストテキストテキストテキストテキストテキストテキストテキスト</span></li>
  <li><span class="date">20XX.00.00</span><span>テキストテキストテキストテキストテキストテキストテキストテキストテキストテキスト</span></li>
  <li><span class="date">20XX.00.00</span><span>テキストテキストテキストテキストテキストテキストテキストテキストテキストテキスト</span></li>
  <li><span class="date">20XX.00.00</span><span>テキストテキストテキストテキストテキストテキストテキストテキストテキストテキスト</span></li>
</ul>

<a class="outline-btn" style="top:2148px">一覧を見る</a>

<section class="shop-band">
  <a class="shop-btn shop-official">公式ショップ</a>
  <a class="shop-btn shop-mall">モールショップ</a>
</section>

<footer class="site-footer">
  <div class="footer-logo">青葉製作所</div>
  <p class="footer-address">〒000-0000 架空県青葉市中央町0-0-0<br>TEL 000-000-0000　FAX 000-000-0000</p>
  <nav class="footer-nav">
    <span>事業紹介</span><span>製品情報</span><span>採用情報</span><span>会社案内</span><span>お問い合わせ</span><span>個人情報保護方針</span><span>サイトマップ</span>
  </nav>
  <p class="copyright">© 青葉製作所 All Rights Reserved.</p>
</footer>

</body>
</html>
```